Continuation of "Why Choose Us" animated gif banners campaign

The original project would not allow me to select any more designs, so I started this new project so you can submit your designs and I will purchase them.

Thanks!

```html
<!DOCTYPE html>
<html lang="en">
<head>
<meta charset="utf-8">
<title>Contact Us Today – Banner Set</title>
<link rel="stylesheet" href="https://fonts.googleapis.com/css2?family=Poppins:wght@700;800&display=swap">
<style>
  :root {
    --page-bg: #ffffff;
    --frame: rgba(255,255,255,0.95);
    --text-light: #ffffff;
    --text-dark: #111111;
    --glow: rgba(255,255,255,0.85);
    --pink-a: #ff3fa8;   --pink-b: #d1127a;
    --purple-a: #a15cf2; --purple-b: #6e26c9;
    --red-a: #f2444f;    --red-b: #c21a2a;
    --orange-a: #ff9a3a; --orange-b: #e0621a;
    --yellow-a: #ffd84a; --yellow-b: #e8a818;
    --green-a: #5ee05a;  --green-b: #24a828;
    --cyan-a: #5fd4f5;   --cyan-b: #1598d0;
    --blue-a: #3d5ef0;   --blue-b: #1a2aa8;
    --maroon-a: #c95a66; --maroon-b: #8e2c38;
    --mauve-a: #d0b8b8;  --mauve-b: #9a7c7e;
    --black-a: #3a3a3a;  --black-b: #050505;
  }
  * { box-sizing: border-box; margin: 0; padding: 0; }
  html, body {
    width: 1200px; height: 3430px; overflow: hidden;
    background: var(--page-bg);
  }
  .banner-set {
    position: relative; width: 1200px; height: 3430px;
    padding-top: 119px;
    display: flex; flex-direction: column; align-items: center; gap: 72px;
  }
  .banner {
    position: relative; width: 1012px; height: 221px;
    font-family: "Poppins", sans-serif;
  }
  .banner-backdrop {
    position: absolute; inset: 0 0 12px 0;
    background:
      radial-gradient(circle at 12% 30%, var(--glow) 0, transparent 9px),
      radial-gradient(circle at 34% 78%, var(--glow) 0, transparent 7px),
      radial-gradient(circle at 58% 18%, var(--glow) 0, transparent 10px),
      radial-gradient(circle at 76% 84%, var(--glow) 0, transparent 8px),
      radial-gradient(circle at 91% 40%, var(--glow) 0, transparent 9px),
      radial-gradient(circle at 24% 58%, rgba(255,255,255,0.6) 0, transparent 5px),
      radial-gradient(circle at 68% 52%, rgba(255,255,255,0.6) 0, transparent 5px),
      radial-gradient(ellipse at 30% 40%, rgba(255,255,255,0.32), transparent 55%),
      radial-gradient(ellipse at 80% 70%, rgba(255,255,255,0.22), transparent 50%),
      radial-gradient(ellipse at 55% 50%, rgba(255,255,255,0.15), transparent 35%),
      linear-gradient(100deg, var(--c-a), var(--c-b) 50%, var(--c-a));
  }
  .banner-frame {
    position: absolute; left: 22px; right: 22px; top: 28px; height: 150px;
    border: 5px solid var(--frame);
  }
  .banner-title {
    position: absolute; left: 0; right: 0; top: 52px;
    text-align: center; color: var(--text-light);
    font-weight: 800; font-size: 86px; line-height: 100px; letter-spacing: -2px;
    white-space: nowrap;
    text-shadow: 0 3px 8px rgba(0,0,0,0.25);
  }
  .banner-phone {
    position: absolute; left: 50%; top: 166px; transform: translateX(-50%);
    width: 340px; height: 55px;
    background: #ffffff; color: var(--text-dark);
    font-weight: 700; font-size: 36px; line-height: 55px; text-align: center;
    white-space: nowrap;
  }
  .pink   { --c-a: var(--pink-a);   --c-b: var(--pink-b); }
  .purple { --c-a: var(--purple-a); --c-b: var(--purple-b); }
  .red    { --c-a: var(--red-a);    --c-b: var(--red-b); }
  .orange { --c-a: var(--orange-a); --c-b: var(--orange-b); }
  .yellow { --c-a: var(--yellow-a); --c-b: var(--yellow-b); }
  .green  { --c-a: var(--green-a);  --c-b: var(--green-b); }
  .cyan   { --c-a: var(--cyan-a);   --c-b: var(--cyan-b); }
  .blue   { --c-a: var(--blue-a);   --c-b: var(--blue-b); }
  .maroon { --c-a: var(--maroon-a); --c-b: var(--maroon-b); }
  .mauve  { --c-a: var(--mauve-a);  --c-b: var(--mauve-b); }
  .black  { --c-a: var(--black-a);  --c-b: var(--black-b); }
</style>
</head>
<body>
<main class="banner-set">
  <section class="banner pink">
    <div class="banner-backdrop" role="img" aria-label="Pink background with glowing circuit-board pattern and sparkles"></div>
    <div class="banner-frame"></div>
    <h2 class="banner-title">CONTACT US TODAY</h2>
    <p class="banner-phone">0198 765 4320</p>
  </section>
  <section class="banner purple">
    <div class="banner-backdrop" role="img" aria-label="Purple background with glowing circuit-board pattern and sparkles"></div>
    <div class="banner-frame"></div>
    <h2 class="banner-title">CONTACT US TODAY</h2>
    <p class="banner-phone">0198 765 4320</p>
  </section>
  <section class="banner red">
    <div class="banner-backdrop" role="img" aria-label="Red background with glowing circuit-board pattern and sparkles"></div>
    <div class="banner-frame"></div>
    <h2 class="banner-title">CONTACT US TODAY</h2>
    <p class="banner-phone">0198 765 4320</p>
  </section>
  <section class="banner orange">
    <div class="banner-backdrop" role="img" aria-label="Orange background with glowing circuit-board pattern and sparkles"></div>
    <div class="banner-frame"></div>
    <h2 class="banner-title">CONTACT US TODAY</h2>
    <p class="banner-phone">0198 765 4320</p>
  </section>
  <section class="banner yellow">
    <div class="banner-backdrop" role="img" aria-label="Yellow background with glowing circuit-board pattern and sparkles"></div>
    <div class="banner-frame"></div>
    <h2 class="banner-title">CONTACT US TODAY</h2>
    <p class="banner-phone">0198 765 4320</p>
  </section>
  <section class="banner green">
    <div class="banner-backdrop" role="img" aria-label="Green background with glowing circuit-board pattern and sparkles"></div>
    <div class="banner-frame"></div>
    <h2 class="banner-title">CONTACT US TODAY</h2>
    <p class="banner-phone">0198 765 4320</p>
  </section>
  <section class="banner cyan">
    <div class="banner-backdrop" role="img" aria-label="Cyan background with glowing circuit-board pattern and sparkles"></div>
    <div class="banner-frame"></div>
    <h2 class="banner-title">CONTACT US TODAY</h2>
    <p class="banner-phone">0198 765 4320</p>
  </section>
  <section class="banner blue">
    <div class="banner-backdrop" role="img" aria-label="Blue background with glowing circuit-board pattern and sparkles"></div>
    <div class="banner-frame"></div>
    <h2 class="banner-title">CONTACT US TODAY</h2>
    <p class="banner-phone">0198 765 4320</p>
  </section>
  <section class="banner maroon">
    <div class="banner-backdrop" role="img" aria-label="Maroon background with glowing circuit-board pattern and sparkles"></div>
    <div class="banner-frame"></div>
    <h2 class="banner-title">CONTACT US TODAY</h2>
    <p class="banner-phone">0198 765 4320</p>
  </section>
  <section class="banner mauve">
    <div class="banner-backdrop" role="img" aria-label="Dusty mauve background with glowing circuit-board pattern and sparkles"></div>
    <div class="banner-frame"></div>
    <h2 class="banner-title">CONTACT US TODAY</h2>
    <p class="banner-phone">0198 765 4320</p>
  </section>
  <section class="banner black">
    <div class="banner-backdrop" role="img" aria-label="Black background with glowing circuit-board pattern and sparkles"></div>
    <div class="banner-frame"></div>
    <h2 class="banner-title">CONTACT US TODAY</h2>
    <p class="banner-phone">0198 765 4320</p>
  </section>
</main>
</body>
</html>
```